Business Card Design needed for logo design project

This project is linked to a href='http://jobs.plankforge.net/job.aspx?id=417902'Keel Drift: Design a logo for our new trailer boat syndication business in Sydney
Our company needs a Business Card Design. Please refer to our original project in the link above.
I would like a relatively simple and classy business card design. could you please also use small symbols for identifying contact info eg. mobile, web and email?
Updates
Please see my new project to design a business card for a trailer boat syndication business in Sydney, Australia.
Industry/Entity Type
Business
Look and feel
Each slider illustrates characteristics of the customer's brand and the style your logo design should communicate.

```html
<!DOCTYPE html>
<html lang="en">
<head>
<meta charset="utf-8">
<title>Keel Drift – Business Card</title>
<link href="https://fonts.googleapis.com/css2?family=Exo+2:ital,wght@0,400;0,700;1,400;1,600&display=swap" rel="stylesheet">
<style>
  :root {
    --backdrop: #2b2b2d;
    --card: #221e23;
    --teal: #3fb0b8;
    --teal-soft: rgba(63, 176, 184, 0.22);
    --grey-soft: rgba(90, 90, 94, 0.35);
    --white: #ffffff;
    --soft-white: #e9e9ea;
    --shadow: rgba(0, 0, 0, 0.45);
  }
  * { margin: 0; padding: 0; box-sizing: border-box; }
  html, body {
    width: 1200px;
    height: 900px;
    overflow: hidden;
    background: var(--backdrop);
    font-family: "Exo 2", Arial, sans-serif;
  }
  .stage {
    position: relative;
    width: 1200px;
    height: 900px;
  }
  .card {
    position: absolute;
    top: 301px;
    width: 515px;
    height: 296px;
    background: var(--card);
    box-shadow: 0 6px 14px var(--shadow);
    overflow: hidden;
  }
  .card--front { left: 73px; }
  .card--back { left: 615px; }

  /* Decorative sweep area behind content */
  .sweep {
    position: absolute;
  }
  .sweep--front-top {
    left: 0; top: 8px; width: 515px; height: 52px;
    background: linear-gradient(90deg, var(--grey-soft) 0%, var(--teal-soft) 60%, var(--teal) 100%);
    opacity: 0.55;
  }
  .sweep--front-bottom {
    left: 40px; top: 185px; width: 475px; height: 110px;
    background: linear-gradient(90deg, var(--grey-soft) 0%, var(--grey-soft) 50%, var(--teal-soft) 100%);
    opacity: 0.8;
  }
  .sweep--back {
    left: 0; top: 0; width: 300px; height: 245px;
    background: linear-gradient(100deg, var(--teal-soft) 0%, var(--grey-soft) 55%, rgba(34, 30, 35, 0) 100%);
  }

  /* Front */
  .front-mark {
    position: absolute;
    left: 62px;
    top: 98px;
    width: 56px;
    height: 56px;
    background: var(--teal);
  }
  .front-brand {
    position: absolute;
    left: 183px;
    top: 92px;
  }
  .front-brand__name {
    font-weight: 700;
    font-size: 60px;
    line-height: 1;
    color: var(--teal);
    letter-spacing: 0.5px;
  }
  .front-brand__tagline {
    margin-top: 5px;
    font-size: 10.5px;
    font-weight: 400;
    color: var(--white);
    letter-spacing: 0.9px;
  }

  /* Back */
  .back-brand {
    position: absolute;
    left: 266px;
    top: 70px;
  }
  .back-brand__name {
    font-weight: 700;
    font-size: 40px;
    line-height: 1;
    color: var(--teal);
  }
  .back-brand__tagline {
    margin-top: 2px;
    font-size: 7.2px;
    color: var(--white);
    letter-spacing: 0.5px;
  }
  .person {
    position: absolute;
    left: 264px;
    top: 135px;
    font-style: italic;
    line-height: 20px;
  }
  .person__name {
    font-weight: 600;
    font-size: 15px;
    color: var(--teal);
  }
  .person__role {
    font-weight: 600;
    font-size: 15px;
    color: var(--white);
  }
  .contacts {
    position: absolute;
    left: 266px;
    top: 190px;
    list-style: none;
  }
  .contacts__item {
    display: flex;
    align-items: center;
    height: 17.5px;
    font-style: italic;
    font-size: 13.5px;
    color: var(--soft-white);
  }
  .contacts__icon {
    width: 11px;
    height: 11px;
    margin-right: 7px;
    flex: none;
  }
</style>
</head>
<body>
  <main class="stage">
    <section class="card card--front" aria-label="Business card front">
      <div class="sweep sweep--front-top" role="img" aria-label="Decorative teal and grey sweeping hull lines"></div>
      <div class="sweep sweep--front-bottom" role="img" aria-label="Decorative grey sweeping lines and trailer wheels"></div>
      <div class="front-mark" aria-hidden="true"></div>
      <div class="front-brand">
        <div class="front-brand__name">Keel Drift</div>
        <div class="front-brand__tagline">TRAILER BOAT SYNDICATION AND MANAGEMENT</div>
      </div>
    </section>

    <section class="card card--back" aria-label="Business card back">
      <div class="sweep sweep--back" role="img" aria-label="Decorative teal and grey sweeping hull lines"></div>
      <div class="back-brand">
        <div class="back-brand__name">Keel Drift</div>
        <div class="back-brand__tagline">TRAILER BOAT SYNDICATION AND MANAGEMENT</div>
      </div>

      <div class="person">
        <div class="person__name">Marcus Whitfield</div>
        <div class="person__role">managing director</div>
      </div>

      <ul class="contacts">
        <li class="contacts__item">
          <svg class="contacts__icon" viewBox="0 0 12 12" aria-hidden="true">
            <rect x="3" y="0.5" width="6" height="11" rx="1" fill="none" stroke="#3fb0b8" stroke-width="1.2"/>
            <circle cx="6" cy="9.5" r="0.7" fill="#3fb0b8"/>
          </svg>
          555 014 27 63
        </li>
        <li class="contacts__item">
          <svg class="contacts__icon" viewBox="0 0 12 12" aria-hidden="true">
            <rect x="0.5" y="2.5" width="11" height="7.5" fill="#3fb0b8"/>
            <path d="M0.8 2.8 L6 6.8 L11.2 2.8" fill="none" stroke="#221e23" stroke-width="1"/>
          </svg>
          mwhitfield@keeldrift.com.au
        </li>
        <li class="contacts__item">
          <svg class="contacts__icon" viewBox="0 0 12 12" aria-hidden="true">
            <circle cx="6" cy="6" r="5.2" fill="none" stroke="#3fb0b8" stroke-width="1.1"/>
            <ellipse cx="6" cy="6" rx="2.3" ry="5.2" fill="none" stroke="#3fb0b8" stroke-width="1"/>
            <line x1="0.8" y1="6" x2="11.2" y2="6" stroke="#3fb0b8" stroke-width="1"/>
          </svg>
          www.keeldrift.com.au
        </li>
      </ul>
    </section>
  </main>
</body>
</html>
```